Sri Lankan Cricket Tour For Girls Aged 14-18 in July 2018

We need a flyer to promote a cricket tour of Sri Lanka in July 2018 for girls aged 14-18.
We want the flyer to call for "expressions of interest".
We would like the Sri Lankan Flag also images of cricket ball and beaches and palm trees etc.
Mention Level 3 Coaches with International experience.
Target market is parents of girls aged 14 to 18 and girls aged 14 to 18

Target Market(s)

Parents of girls aged 14 to 18 and girls aged 14 to 18

Industry/Entity Type

Travel

Font styles to use
Serif
Sans Serif

Colors
0355a3
ec1f27
fbed22

Requirements
Must have
• Sri Lankan Flag, Halvey Athletics Logo, email address boyd@halveyathletics.com.au.
• - 10 Day Tour
• - Play on First Class Grounds
• - Level 3 Coaches With International Experience
• - For More Information Contact Boyd boyd@halveyathletics.com.au
Nice to have
• Picture of girls playing cricket, sun and beach
Should not have
• Cartoon type images
• Photo's of actual cricketers

```html
<!DOCTYPE html>
<html lang="en">
<head>
<meta charset="utf-8">
<title>Cricket Tour Of Sri Lanka – July 2018</title>
<link href="https://fonts.googleapis.com/css2?family=Arimo:wght@400;700&display=swap" rel="stylesheet">
<style>
  :root {
    --brand-blue: #0355a3;
    --brand-red: #ec1f27;
    --brand-yellow: #fbed22;
    --white: #ffffff;
    --logo-panel: #1b1b1d;
    --sky-top: #1d5fb8;
    --sky-mid: #5fa4e0;
    --cloud: #dfeefa;
    --sea: #2ab3c9;
    --sea-light: #8fdde0;
    --sand: #e9ddc6;
    --flag-gold: #f7b718;
    --flag-green: #00534e;
    --flag-orange: #f57a1f;
    --flag-maroon: #8d153a;
  }
  * { margin: 0; padding: 0; box-sizing: border-box; }
  html, body { width: 1200px; height: 851px; overflow: hidden; background: #fff; }
  .flyer {
    position: relative;
    width: 1200px;
    height: 851px;
    overflow: hidden;
    font-family: "Arimo", Arial, sans-serif;
    color: var(--white);
  }
  .beach-scene {
    position: absolute; inset: 0;
    background: linear-gradient(180deg,
      var(--sky-top) 0%, var(--sky-mid) 38%, var(--cloud) 58%,
      var(--sea) 64%, var(--sea-light) 78%, var(--sand) 92%, var(--sand) 100%);
  }
  .headline {
    position: absolute; left: 51px; top: 44px;
    font-size: 38px; font-weight: 700; line-height: 1.45;
  }
  .flag {
    position: absolute; left: 51px; top: 190px;
    width: 345px; height: 132px;
  }
  .tour-date {
    position: absolute; left: 46px; top: 382px;
    font-size: 120px; font-weight: 400; letter-spacing: -2px;
    color: var(--brand-yellow); line-height: 1;
  }
  .highlights {
    position: absolute; left: 51px; top: 591px;
    list-style: none; font-size: 28px; font-weight: 700; line-height: 42px;
  }
  .contact-bar {
    position: absolute; left: 0; top: 730px;
    width: 674px; height: 121px;
    background: var(--brand-blue);
    border-top-right-radius: 40px;
    padding: 14px 0 0 51px;
  }
  .contact-bar .lead { font-size: 26px; line-height: 1.2; }
  .contact-bar .contact { font-size: 36px; font-weight: 700; margin-top: 10px; }
  .logo-panel {
    position: absolute; left: 720px; top: 591px;
    width: 446px; height: 232px;
    background: var(--logo-panel);
    display: flex; align-items: center; justify-content: center;
  }
  .logo-name {
    font-size: 36px; font-weight: 700; color: var(--white);
  }
</style>
</head>
<body>
<main class="flyer">
  <div class="beach-scene" role="img" aria-label="Tropical beach with palm tree, blue sky, clouds and turquoise sea"></div>

  <h1 class="headline">Cricket Tour Of Sri Lanka<br>For Girls Aged 14-18</h1>

  <svg class="flag" viewBox="0 0 345 132" aria-label="Flag of Sri Lanka">
    <rect width="345" height="132" fill="var(--flag-gold)"/>
    <rect x="8" y="8" width="32" height="116" fill="var(--flag-green)"/>
    <rect x="40" y="8" width="32" height="116" fill="var(--flag-orange)"/>
    <rect x="82" y="8" width="255" height="116" fill="var(--flag-maroon)"/>
    <rect x="170" y="26" width="80" height="80" rx="6" fill="var(--flag-gold)" opacity="0.85" role="img" aria-label="Lion emblem of the flag"/>
  </svg>

  <p class="tour-date">July 2018</p>

  <ul class="highlights">
    <li>First Class Grounds</li>
    <li>10 Day Tour</li>
    <li>Level 3 Coaches with International experience</li>
  </ul>

  <section class="contact-bar">
    <p class="lead">For More Information Contact</p>
    <p class="contact">Boyd boyd@halveyathletics.com.au</p>
  </section>

  <div class="logo-panel">
    <span class="logo-name">Halvey Athletics</span>
  </div>
</main>
</body>
</html>
```